Commercial Business Card - stand out, clean, simple, unique.

commercial real estate group located in Texas. Called 4 Ridges Real Estate. We want a unique yet clean and professional card. On one side I would like the 4R to be by itself or to look as unique or tasteful as possible. We have the logo in white, black, and color in case a black background or something similar looks best on one side. We need a space for our name, email, cell. website. And possibly room for a phrase or city.

Contact Information for Business Card

Name, Title, Email, Phone Number, website

```html
<!DOCTYPE html>
<html lang="en">
<head>
<meta charset="utf-8">
<title>4 Ridges Real Estate — Business Cards</title>
<link href="https://fonts.googleapis.com/css2?family=Open+Sans:wght@300;400;600;700&display=swap" rel="stylesheet">
<style>
  :root {
    --canvas: #e6e5e2;
    --paper: #ffffff;
    --ink: #111111;
    --muted: #8a8a8a;
    --rule: #c9c9c9;
    --reverse: #050505;
    --reverse-ink: #ffffff;
  }
  * { box-sizing: border-box; margin: 0; padding: 0; }
  html, body {
    width: 1200px;
    height: 980px;
    overflow: hidden;
    background: var(--canvas);
    font-family: "Open Sans", Arial, sans-serif;
    color: var(--ink);
  }
  .card-set {
    width: 1200px;
    height: 980px;
    display: flex;
    align-items: center;
    justify-content: center;
    gap: 60px;
  }
  .card {
    width: 320px;
    height: 520px;
    background: var(--paper);
    position: relative;
    box-shadow: 0 2px 6px rgba(0,0,0,0.12);
  }
  /* Contact side */
  .card--contact {
    padding: 40px 36px 34px;
    display: flex;
    flex-direction: column;
  }
  .holder-name {
    font-size: 30px;
    font-weight: 700;
    line-height: 1.05;
  }
  .holder-title {
    font-size: 19px;
    font-weight: 300;
    font-style: italic;
    color: var(--muted);
    margin-top: 2px;
  }
  .contact-list {
    list-style: none;
    margin-top: 44px;
  }
  .contact-list li {
    font-size: 17px;
    font-weight: 300;
    color: var(--muted);
    height: 40px;
    display: flex;
    align-items: center;
  }
  .contact-rule {
    height: 1px;
    background: var(--rule);
    margin: 14px 0 0;
  }
  .contact-rule + .contact-list { margin-top: 16px; }
  .card-brand {
    margin-top: auto;
    text-align: center;
  }
  .brand-mark {
    font-size: 58px;
    font-weight: 600;
    line-height: 1;
    letter-spacing: -1px;
  }
  .brand-line {
    margin-top: 8px;
    font-size: 11px;
    font-weight: 600;
    letter-spacing: 2px;
    text-transform: uppercase;
    display: flex;
    align-items: center;
    justify-content: center;
    gap: 8px;
  }
  .brand-line::before,
  .brand-line::after {
    content: "";
    width: 18px;
    height: 1px;
    background: var(--ink);
  }
  /* Monogram sides */
  .card--monogram {
    display: flex;
    align-items: center;
    justify-content: center;
  }
  .card--reverse { background: var(--reverse); }
  .monogram {
    font-size: 190px;
    font-weight: 600;
    line-height: 1;
    letter-spacing: -6px;
    color: var(--ink);
  }
  .card--reverse .monogram { color: var(--reverse-ink); }
</style>
</head>
<body>
  <main class="card-set">
    <section class="card card--contact" aria-label="Contact side">
      <h1 class="holder-name">Name</h1>
      <p class="holder-title">Title</p>
      <div class="contact-rule"></div>
      <ul class="contact-list">
        <li>e:</li>
        <li>p:</li>
        <li>w:</li>
      </ul>
      <div class="contact-rule"></div>
      <div class="card-brand">
        <div class="brand-mark">4R</div>
        <div class="brand-line">4 Ridges Real Estate</div>
      </div>
    </section>

    <section class="card card--monogram card--reverse" aria-label="Monogram side, black">
      <span class="monogram">4R</span>
    </section>

    <section class="card card--monogram" aria-label="Monogram side, white">
      <span class="monogram">4R</span>
    </section>
  </main>
</body>
</html>
```